Price sign

Looking for a fresh new pricing sign.. with new prices size 2ft tall x 4ft wide , express lube $40.95, automatic transmission $129.95, radiator $109.95, Torvex plus express lube $79.95, std trans/ diff $79.95, tuneup 4cyl $149.95, 6cyl $175.95 ,

```html
<!DOCTYPE html>
<html lang="en">
<head>
<meta charset="utf-8">
<title>Service Price Sign</title>
<link rel="stylesheet" href="https://fonts.googleapis.com/css2?family=Archivo:ital,wght@1,800;1,900&family=Sansita:ital,wght@1,800;1,900&display=swap">
<style>
  :root {
    --black: #0b0b0b;
    --red: #d40000;
    --yellow: #f2cf1d;
    --white: #ffffff;
    --steel-dark: #151515;
    --steel-mid: #2e2e2e;
  }
  * { margin: 0; padding: 0; box-sizing: border-box; }
  html, body { width: 1200px; height: 600px; overflow: hidden; background: var(--black); }
  .sign { position: relative; width: 1200px; height: 600px; overflow: hidden; background: var(--black); }
  .engine-backdrop {
    position: absolute; inset: 0;
    background: radial-gradient(ellipse at 55% 45%, var(--steel-mid) 0%, var(--steel-dark) 45%, var(--black) 80%);
  }
  .block { position: absolute; text-align: center; white-space: nowrap; }
  .col-left { left: 0; width: 410px; }
  .col-mid { left: 420px; width: 370px; }
  .col-right { left: 830px; width: 350px; }

  .headline { font-family: "Archivo", sans-serif; font-weight: 900; font-style: italic; line-height: 1; letter-spacing: -1px; }
  .detail { font-family: "Sansita", sans-serif; font-weight: 900; font-style: italic; line-height: 1; color: var(--white); }
  .service-time { font-size: 30px; }
  .service-interval { font-size: 19px; }
  .price { font-family: "Sansita", sans-serif; font-weight: 900; font-style: italic; line-height: 1; letter-spacing: -1px; }
  .price sup { font-size: 0.5em; vertical-align: 0.55em; margin-right: 2px; }
  .red { color: var(--red); }
  .yellow { color: var(--yellow); }
  .white { color: var(--white); }

  .checker { position: absolute; background: linear-gradient(90deg, #e6e6e6, #9a9a9a); }
  .rule { position: absolute; height: 3px; }
  .rule.red-rule { background: var(--red); }
  .rule.yellow-rule { background: var(--yellow); }

  .brand-box {
    position: absolute; left: 33px; top: 401px; width: 340px; height: 44px;
    background: var(--white); display: flex; align-items: center; justify-content: center; gap: 12px;
    font-family: "Sansita", sans-serif; font-weight: 900; font-style: italic; font-size: 26px; color: var(--black);
  }
  .brand-name { color: var(--black); }
  .cyl-divider { position: absolute; left: 1003px; top: 515px; width: 2px; height: 58px; background: var(--white); transform: skewX(-8deg); }
  .speed-lines { position: absolute; left: 830px; top: 78px; width: 350px; height: 132px; }
</style>
</head>
<body>
<main class="sign">
  <div class="engine-backdrop" role="img" aria-label="Dark photo of engine gears and transmission parts"></div>

  <!-- Express Lube -->
  <div class="checker" style="left:17px;top:20px;width:80px;height:122px;" role="img" aria-label="Checkered flag pattern"></div>
  <div class="checker" style="left:322px;top:20px;width:62px;height:122px;" role="img" aria-label="Checkered flag pattern"></div>
  <div class="block col-left headline white" style="top:18px;left:20px;font-family:'Sansita',sans-serif;font-size:52px;">Express</div>
  <div class="block col-left headline red" style="top:66px;left:-12px;font-size:88px;letter-spacing:-4px;">LUBE</div>
  <div class="block col-left detail service-time" style="top:148px;">14 POINT SERVICE</div>
  <div class="block col-left detail service-interval" style="top:180px;left:-12px;">Service Every 3000 Miles</div>
  <div class="block col-left price red" style="top:205px;left:-20px;font-size:78px;"><sup>$</sup>40.95</div>

  <div class="checker" style="left:0;top:291px;width:405px;height:19px;" role="img" aria-label="Checkered band"></div>

  <!-- Roscoe's Best -->
  <div class="rule yellow-rule" style="left:33px;top:338px;width:340px;"></div>
  <div class="block headline yellow" style="left:33px;width:340px;top:344px;font-size:46px;">ROSCOE'S BEST</div>
  <div class="rule yellow-rule" style="left:33px;top:392px;width:340px;"></div>
  <div class="brand-box"><span class="brand-name">Torvex plus</span><span>Express Lube</span></div>
  <div class="block col-left detail service-time" style="top:455px;">14 POINT SERVICE</div>
  <div class="block col-left detail service-interval" style="top:487px;left:-12px;">Service Every 3000 Miles</div>
  <div class="block col-left price yellow" style="top:512px;left:-10px;font-size:76px;"><sup>$</sup>79.95</div>

  <!-- Automatic Transmission -->
  <div class="block col-mid headline yellow" style="top:22px;font-family:'Sansita',sans-serif;font-size:56px;">Automatic</div>
  <div class="block col-mid headline yellow" style="top:76px;font-size:46px;letter-spacing:-2px;">TRANSMISSION</div>
  <div class="block col-mid detail service-time" style="top:140px;">30 MINUTE SERVICE</div>
  <div class="block col-mid detail service-interval" style="top:172px;left:408px;">Service Every 25000 Miles</div>
  <div class="block col-mid price yellow" style="top:205px;font-size:80px;"><sup>$</sup>129.95</div>
  <div class="rule red-rule" style="left:427px;top:301px;width:341px;"></div>

  <!-- Standard Transmission -->
  <div class="block col-mid headline white" style="top:326px;font-family:'Sansita',sans-serif;font-size:52px;">Standard</div>
  <div class="block col-mid headline white" style="top:372px;font-size:40px;letter-spacing:-2px;">TRANSMISSION</div>
  <div class="block col-mid headline red" style="top:408px;font-size:38px;letter-spacing:-2px;">OR DIFERENTIAL</div>
  <div class="block col-mid detail service-time" style="top:455px;">15 MINUTE SERVICE</div>
  <div class="block col-mid detail service-interval" style="top:487px;left:408px;">Service Every 25000 Miles</div>
  <div class="block col-mid price red" style="top:512px;left:385px;font-size:78px;"><sup>$</sup>79.95</div>

  <!-- Radiator Service -->
  <div class="block col-right headline red" style="top:24px;left:840px;font-size:64px;letter-spacing:-2px;">RADIATOR</div>
  <svg class="speed-lines" viewBox="0 0 350 132" aria-hidden="true">
    <g stroke="#ffffff" stroke-width="1.5">
      <line x1="22" y1="2" x2="2" y2="130"/><line x1="30" y1="2" x2="10" y2="130"/><line x1="38" y1="2" x2="18" y2="130"/><line x1="46" y1="2" x2="26" y2="130"/>
      <line x1="322" y1="2" x2="302" y2="130"/><line x1="330" y1="2" x2="310" y2="130"/><line x1="338" y1="2" x2="318" y2="130"/><line x1="346" y1="2" x2="326" y2="130"/>
    </g>
  </svg>
  <div class="block col-right headline red" style="top:86px;font-family:'Sansita',sans-serif;font-size:42px;">Service</div>
  <div class="block col-right detail service-time" style="top:142px;">30 MINUTE SERVICE</div>
  <div class="block col-right detail service-interval" style="top:172px;">Service Every 25000 Miles</div>
  <div class="block col-right price red" style="top:203px;font-size:74px;"><sup>$</sup>109.95</div>
  <div class="rule yellow-rule" style="left:832px;top:301px;width:340px;"></div>

  <!-- Roscoe's Tune Up -->
  <div class="block col-right headline yellow" style="top:326px;font-size:42px;">ROSCOE'S</div>
  <div class="block col-right headline white" style="top:368px;font-size:64px;letter-spacing:-3px;">TUNE UP</div>
  <div class="rule yellow-rule" style="left:851px;top:432px;width:302px;"></div>
  <div class="block col-right detail service-time" style="top:447px;">60 MINUTE SERVICE</div>
  <div class="block col-right detail service-interval" style="top:480px;">Service Every 25000 Miles</div>
  <div class="block detail white" style="left:845px;width:140px;top:513px;font-size:30px;">4CYL</div>
  <div class="block detail white" style="left:1015px;width:140px;top:513px;font-size:30px;">6CYL</div>
  <div class="block price yellow" style="left:835px;width:160px;top:543px;font-size:36px;"><sup>$</sup>149.95</div>
  <div class="block price yellow" style="left:1005px;width:160px;top:543px;font-size:36px;"><sup>$</sup>175.95</div>
  <div class="cyl-divider"></div>
</main>
</body>
</html>
```